Trade show banner and popup for Plexa Works

Use the existing logo and graphic elements and text of sales arguments from our web site www.plexaworks-demo.com to create a backdrop banner and popup banner.

Both banners are trim size 181.7 x 76.2 cm. One is vertical, the other is horizontal. The full bleed size is 767 x 1824 mm 2265 x 5385 pixels.

We have a 2m by 2m corner stand on a tradeshow. The banner will be on one wall, the vertical against the other wall by the aisle.

Target Market(s)

This display is for a manufacturing trade show. The typical visitors are middle age engineers.

Industry/Entity Type

Trade

Requirements
Must have
• Our logo.
Nice to have
• One of the main benefits of our system is that it can be created for no charge with an online signup which is available at the show. We want to tempt people off the aisles to do this. So the vertical banner could have the words "Create your own online ERP system here for no charge"
Should not have
• Small text, these banners should attract attention of passers by in a trade show.

```html
<!DOCTYPE html>
<html lang="en">
<head>
<meta charset="utf-8">
<title>Plexa Works – Trade Show Banners</title>
<link rel="stylesheet" href="https://fonts.googleapis.com/css2?family=Open+Sans:wght@600;700;800&display=swap">
<style>
  :root {
    --page-bg: #efefef;
    --ink-dark: #1d2430;
    --ink-light: #ffffff;
    --mark-tan: #b8a874;
    --sky-deep: #2f67b8;
    --sky-mid: #5f98d6;
    --sky-pale: #cfe2f2;
    --sea: #2a6f9e;
    --grass: #6aa532;
    --grass-dark: #3f7a1e;
  }
  * { margin: 0; padding: 0; box-sizing: border-box; }
  html, body {
    width: 1200px; height: 900px; overflow: hidden;
    background: var(--page-bg);
    font-family: "Open Sans", Arial, sans-serif;
  }
  .stage { position: relative; width: 1200px; height: 900px; }

  .banner {
    position: absolute; overflow: hidden;
    box-shadow: 0 4px 14px rgba(0,0,0,0.25);
  }
  .banner-horizontal { left: 22px; top: 291px; width: 788px; height: 334px; }
  .banner-vertical { left: 842px; top: 62px; width: 334px; height: 791px; }

  .scene-photo { position: absolute; inset: 0; }
  .banner-horizontal .scene-photo {
    background: linear-gradient(180deg,
      var(--sky-deep) 0%, var(--sky-mid) 35%, var(--sky-pale) 62%,
      var(--sea) 66%, var(--sea) 84%, var(--grass) 90%, var(--grass-dark) 100%);
  }
  .banner-vertical .scene-photo {
    background: linear-gradient(180deg,
      var(--sky-deep) 0%, var(--sky-mid) 45%, var(--sky-pale) 68%,
      var(--grass) 76%, var(--grass-dark) 100%);
  }

  .brand { position: absolute; display: flex; align-items: center; gap: 10px; }
  .brand-dot {
    width: 46px; height: 46px; border-radius: 50%;
    background: var(--mark-tan);
  }
  .brand-name {
    font-weight: 700; font-size: 24px; line-height: 22px;
    color: var(--ink-dark);
  }
  .banner-horizontal .brand { left: 538px; top: 32px; }
  .banner-vertical .brand { left: 58px; top: 44px; }

  .headline { position: absolute; text-transform: uppercase; }
  .headline-line { display: block; font-weight: 800; color: var(--ink-dark); }
  .headline-offer { display: block; font-weight: 800; color: var(--ink-light); }

  .banner-horizontal .headline { right: 46px; top: 174px; text-align: right; }
  .banner-horizontal .headline-line { font-size: 18px; letter-spacing: 0.3px; }
  .banner-horizontal .headline-offer { font-size: 29px; line-height: 40px; }

  .banner-vertical .headline { left: 24px; right: 20px; top: 206px; }
  .banner-vertical .headline-line.large { font-size: 26px; line-height: 30px; }
  .banner-vertical .headline-line.small { font-size: 20px; line-height: 24px; }
  .banner-vertical .headline-offer { font-size: 34px; line-height: 42px; }
</style>
</head>
<body>
<main class="stage">

  <section class="banner banner-horizontal">
    <div class="scene-photo" role="img" aria-label="Photo: woman with a laptop standing on a grassy hill above a blue sea under a sunny sky"></div>
    <div class="brand">
      <span class="brand-dot"></span>
      <span class="brand-name">Plexa<br>Works</span>
    </div>
    <h1 class="headline">
      <span class="headline-line">Create your own online ERP system here</span>
      <span class="headline-offer">For no charge</span>
    </h1>
  </section>

  <section class="banner banner-vertical">
    <div class="scene-photo" role="img" aria-label="Photo: businesswoman standing in tall green grass shading her eyes, blue sky with clouds"></div>
    <div class="brand">
      <span class="brand-dot"></span>
      <span class="brand-name">Plexa<br>Works</span>
    </div>
    <h2 class="headline">
      <span class="headline-line large">Create your own</span>
      <span class="headline-line small">Online ERP system here</span>
      <span class="headline-offer">For no charge</span>
    </h2>
  </section>

</main>
</body>
</html>
```